Design 6.5 x 9 Postcard for Business

You will need to design a 6.5" x 9" postcard for our insulation business, Vornel Thermal, LLC based on design requirements. We will be using Postwisp and have attached template for guide. Must include phone number, web address, company logo, tidal keep partner logo and marketing call to action. Specificallyl marketing 75-100% off insulation & weatheriation services with FREE Home Energy Assessment. Absolutely no cost. I have given examples of other companies on attachment as well for inspiration. I will also need to ensure that somewhere clear is "Our company just insulated a home on your mail route and we'd like to offer you a FREE assessment!"

Here are competitior websites for inspiration.

https://www.quellohome.example/?gclid=EAIaIQobChMI3PqbgNaL6gIVgZOzCh3-AQG1EAAYASAAEgKziPD_BwE

https://www.brambleloftheat.example/

```html
<!DOCTYPE html>
<html lang="en">
<head>
<meta charset="utf-8">
<title>Vornel Thermal Postcard</title>
<link href="https://fonts.googleapis.com/css2?family=Fira+Sans:wght@400;500;600;700&family=Oswald:wght@500;600;700&display=swap" rel="stylesheet">
<style>
  :root {
    --brand-blue: #1d4f8c;
    --navy-band: #174a86;
    --ink-dark: #333338;
    --ink-body: #2b2b2b;
    --tag-grey: #7b7b7b;
    --rule-grey: #8a8a8a;
    --partner-green: #4c9a2a;
    --partner-brown: #5b3a1f;
    --paper: #ffffff;
    --table: #7a7a7a;
  }
  * { box-sizing: border-box; margin: 0; padding: 0; }
  html, body { width: 1200px; height: 904px; overflow: hidden; }
  body {
    background: var(--table);
    font-family: "Fira Sans", Arial, sans-serif;
    color: var(--ink-body);
    position: relative;
  }
  .postcard {
    position: absolute;
    width: 506px;
    height: 372px;
    background: var(--paper);
    overflow: hidden;
    box-shadow: 0 2px 6px rgba(0,0,0,.25);
  }
  .postcard--front { left: 146px; top: 61px; }
  .postcard--back { left: 565px; top: 470px; }
  .postcard .shapes { position: absolute; inset: 0; }
  .abs { position: absolute; }

  /* brand name */
  .brand {
    display: flex; align-items: center; gap: 6px;
    font-weight: 600; color: var(--brand-blue); white-space: nowrap;
  }
  .brand-square { background: var(--brand-blue); display: inline-block; }

  /* front */
  .front-brand { left: 26px; top: 46px; font-size: 21px; }
  .front-brand .brand-square { width: 15px; height: 15px; }
  .kicker { left: 27px; top: 106px; font-size: 17px; font-weight: 700; color: var(--brand-blue); }
  .headline { font-family: "Oswald", "Arial Narrow", sans-serif; font-weight: 700; line-height: 1; white-space: nowrap; }
  .headline--save { left: 26px; top: 127px; font-size: 30px; color: var(--ink-dark); }
  .headline--bills { left: 25px; top: 158px; font-size: 34px; color: var(--brand-blue); }
  .subhead { left: 27px; top: 197px; font-size: 11.6px; font-weight: 600; color: #3a3a3a; }
  .tag {
    top: 219px; height: 18px; background: var(--tag-grey); color: #fff;
    font-size: 10px; font-weight: 500; border-radius: 2px;
    display: flex; align-items: center; justify-content: center;
  }
  .tag--obligation { left: 26px; width: 86px; }
  .tag--estimate { left: 117px; width: 105px; }
  .offer {
    left: 27px; top: 250px; width: 223px; height: 26px;
    border: 1px solid var(--brand-blue); border-radius: 3px; display: flex; overflow: hidden;
  }
  .offer-amount {
    width: 88px; background: var(--brand-blue); color: #fff;
    font-family: "Oswald", "Arial Narrow", sans-serif; font-weight: 500;
    font-size: 18px; display: flex; align-items: center; justify-content: center; gap: 3px;
  }
  .offer-amount small { font-size: 11px; font-weight: 500; margin-top: 4px; }
  .offer-detail { flex: 1; font-size: 6.4px; line-height: 8.4px; padding: 4px 0 0 5px; color: #222; }
  .about { left: 27px; top: 281px; width: 236px; font-size: 6.7px; line-height: 8.8px; text-align: justify; }

  .contact { color: #fff; font-size: 8px; font-weight: 400; white-space: nowrap; display: flex; align-items: center; gap: 7px; }
  .contact span { display: inline-flex; align-items: center; gap: 3px; }
  .contact .phone { font-weight: 600; font-size: 8.4px; }
  .front-address { left: 26px; top: 333px; }
  .front-lines { left: 26px; top: 348px; }

  .partner { left: 362px; top: 336px; width: 92px; text-align: center; }
  .partner-name { font-size: 13px; font-weight: 700; color: var(--partner-brown); display: flex; align-items: center; justify-content: center; gap: 4px; }
  .partner-dot { width: 8px; height: 8px; border-radius: 50%; background: var(--partner-green); }
  .partner-role { font-size: 11px; font-weight: 700; color: var(--partner-green); letter-spacing: .4px; margin-top: 1px; }

  /* back */
  .section-tab {
    height: 15px; background: var(--brand-blue); color: #fff;
    font-size: 9.4px; font-weight: 600; padding-left: 4px;
    display: flex; align-items: center; white-space: nowrap;
    clip-path: polygon(0 0, 94% 0, 100% 100%, 0 100%);
  }
  .tab-process { left: 27px; top: 26px; width: 88px; }
  .tab-services { left: 27px; top: 239px; width: 122px; }
  .step-tab {
    left: 27px; width: 12px; background: var(--tag-grey); color: #fff;
    font-size: 6.6px; font-weight: 600; writing-mode: vertical-rl; transform: rotate(180deg);
    display: flex; align-items: center; justify-content: center; letter-spacing: .3px;
  }
  .step-title { left: 47px; font-size: 7.4px; font-weight: 600; color: #1e1e1e; }
  .step-body { left: 47px; width: 200px; font-size: 5.9px; font-weight: 400; line-height: 8.3px; text-align: justify; color: #333; }
  .services-intro { left: 27px; top: 259px; width: 260px; font-size: 6.4px; font-weight: 400; color: #222; white-space: nowrap; }
  .service-label { top: 307px; font-size: 6.3px; color: #222; white-space: nowrap; transform: translateX(-50%); }
  .back-address { left: 26px; top: 334px; }
  .back-lines { left: 26px; top: 349px; }

  .route-notice {
    left: 318px; top: 40px; width: 165px;
    font-size: 9px; line-height: 12px; font-weight: 600; color: var(--brand-blue);
  }
  .back-brand { left: 312px; top: 262px; font-size: 12px; }
  .back-brand .brand-square { width: 9px; height: 9px; }
  .indicia {
    left: 427px; top: 251px; width: 50px; height: 39px; border: .8px solid #333;
    font-size: 4.6px; line-height: 7px; text-align: center; color: #222; padding-top: 1px;
  }
  .route-line { left: 317px; top: 316px; font-size: 5.2px; color: #222; letter-spacing: .1px; white-space: nowrap; }
  .recipient { left: 317px; top: 333px; font-size: 5.6px; line-height: 8px; color: #222; }
</style>
</head>
<body>

<section class="postcard postcard--front" aria-label="Postcard front">
  <svg class="shapes" width="506" height="372" viewBox="0 0 506 372">
    <defs>
      <linearGradient id="photo-tones" x1="0" y1="0" x2="0" y2="1">
        <stop offset="0" stop-color="#a9c6e6"/>
        <stop offset=".45" stop-color="#e4e6e8"/>
        <stop offset=".75" stop-color="#9d7e6e"/>
        <stop offset="1" stop-color="#6f9a3e"/>
      </linearGradient>
    </defs>
    <polygon points="199,0 506,0 506,323 284,323" fill="url(#photo-tones)" role="img" aria-label="Photo of a two-storey house with a hand holding a thermal imaging camera showing the home's heat map"/>
    <polygon points="0,323 284,323 294,372 0,372" fill="var(--navy-band)"/>
    <circle cx="408" cy="340" r="46" fill="#fff"/>
  </svg>

  <div class="abs brand front-brand"><span class="brand-square"></span>Vornel Thermal</div>
  <div class="abs kicker">WE CAN HELP YOU</div>
  <div class="abs headline headline--save">SAVE ON YOUR</div>
  <div class="abs headline headline--bills">ENERGY BILLS</div>
  <div class="abs subhead">by improving your energy efficiency</div>
  <div class="abs tag tag--obligation">No-Obligation</div>
  <div class="abs tag tag--estimate">No-Cost Estimate!</div>
  <div class="abs offer">
    <div class="offer-amount">75-100% <small>OFF</small></div>
    <div class="offer-detail">insulation &amp; weatheriation services<br>with FREE Home Energy Assessment.</div>
  </div>
  <p class="abs about">Vornel Thermal is a small, locally owned business in Eastmere, Massachusetts. We are passionate about improving our local Greater Eastmere community and about making it a more environmentally committed area.</p>

  <div class="abs contact front-address">
    <span><svg width="9" height="10" viewBox="0 0 9 10"><path d="M4.5 .6a3 3 0 0 0-3 3c0 2.2 3 5 3 5s3-2.8 3-5a3 3 0 0 0-3-3z" fill="none" stroke="#fff" stroke-width=".9"/><circle cx="4.5" cy="3.6" r="1" fill="#fff"/></svg>42 Harbor Lane, Suite B2, Eastmere, MA 02700</span>
  </div>
  <div class="abs contact front-lines">
    <span class="phone"><svg width="8" height="8" viewBox="0 0 8 8"><path d="M1.5 .8l1.4 1.6-.7 1a4 4 0 0 0 2.4 2.4l1-.7 1.6 1.4-.8 1C3.8 7.3.7 4.2.5 1.6z" fill="none" stroke="#fff" stroke-width=".8"/></svg>555-014-2267</span>
    <span><svg width="9" height="7" viewBox="0 0 9 7"><rect x=".5" y=".5" width="8" height="6" fill="none" stroke="#fff" stroke-width=".8"/><path d="M.5.5l4 3.4 4-3.4" fill="none" stroke="#fff" stroke-width=".8"/></svg>info@vornel.example</span>
    <span><svg width="8" height="8" viewBox="0 0 8 8"><circle cx="4" cy="4" r="3.5" fill="none" stroke="#fff" stroke-width=".7"/><ellipse cx="4" cy="4" rx="1.5" ry="3.5" fill="none" stroke="#fff" stroke-width=".7"/><path d="M.5 4h7" stroke="#fff" stroke-width=".7"/></svg>www.vornel.example</span>
  </div>

  <div class="abs partner">
    <div class="partner-name"><span class="partner-dot"></span>tidal keep</div>
    <div class="partner-role">PARTNER</div>
  </div>
</section>

<section class="postcard postcard--back" aria-label="Postcard back">
  <svg class="shapes" width="506" height="372" viewBox="0 0 506 372">
    <polygon points="240,0 245,0 300,372 295,372" fill="var(--rule-grey)"/>
    <polygon points="0,323 287,323 295,372 0,372" fill="var(--navy-band)"/>
    <g fill="none" stroke="#666" stroke-width="1">
      <circle cx="49" cy="288" r="14" fill="#e9e9e9"/><circle cx="49" cy="288" r="11.5"/>
      <path d="M43 283c2-3 6-3 8-1 3-1 5 1 4 4 2 2 0 6-3 5-2 3-6 2-7 0-3 0-4-4-2-6z"/>
      <circle cx="117" cy="288" r="14" fill="#e9e9e9"/><circle cx="117" cy="288" r="11.5"/>
      <rect x="112" y="280" width="10" height="16"/><circle cx="120" cy="288" r=".8" fill="#666"/>
      <circle cx="187" cy="288" r="14" fill="#e9e9e9"/><circle cx="187" cy="288" r="11.5"/>
      <path d="M179 289l8-7 8 7M181 288v6h12v-6"/><rect x="185" y="290" width="4" height="4"/>
      <circle cx="246" cy="288" r="14" fill="#e9e9e9"/><circle cx="246" cy="288" r="11.5"/>
      <path d="M238 285h9a2 2 0 1 0-2-2M238 289h12a2 2 0 1 1-2 2M240 293h5"/>
    </g>
  </svg>

  <div class="abs section-tab tab-process">HOW WE WORK</div>

  <div class="abs step-tab" style="top:47px;height:42px;">STEP 1</div>
  <div class="abs step-title" style="top:48px;">Perform in-home audit</div>
  <p class="abs step-body" style="top:58px;">We begin our journey with you by performing an in-home audit. A member of our team, a fully qualified technician, will schedule a time that works for you to come and assess your home. The assessment will include various tests to decide how best to make your home more energy-efficient.</p>

  <div class="abs step-tab" style="top:108px;height:42px;">STEP 2</div>
  <div class="abs step-title" style="top:110px;">Gain your approval</div>
  <p class="abs step-body" style="top:121px;width:205px;">Following the in-home audit, Vornel Thermal will provide you with a written evaluation of how your home's energy efficiency can be improved. In that evaluation, we will include the cost after any incentives or discounts that you are eligible for, and a form to confirm whether you would like to work with us to improve your home's energy efficiency using insulation and weatherization tools.</p>

  <div class="abs step-tab" style="top:180px;height:42px;">STEP 3</div>
  <div class="abs step-title" style="top:182px;">Improve energy efficiency</div>
  <p class="abs step-body" style="top:193px;width:212px;">After receiving your request to start work, a member of our team will contact you to schedule the work appointment. Our team will perform the work agreed upon in the evaluation, and leave your home more energy efficient!</p>

  <div class="abs section-tab tab-services">PRODUCTS &amp; SERVICES</div>
  <div class="abs services-intro">Vornel Thermal provides full services regarding weatherization and insulation including:</div>
  <div class="abs service-label" style="left:49px;">Wall Insulation</div>
  <div class="abs service-label" style="left:117px;">General Construction</div>
  <div class="abs service-label" style="left:187px;">Attic Insulation</div>
  <div class="abs service-label" style="left:246px;">Air sealing</div>

  <div class="abs contact back-address">
    <span><svg width="9" height="10" viewBox="0 0 9 10"><path d="M4.5 .6a3 3 0 0 0-3 3c0 2.2 3 5 3 5s3-2.8 3-5a3 3 0 0 0-3-3z" fill="none" stroke="#fff" stroke-width=".9"/><circle cx="4.5" cy="3.6" r="1" fill="#fff"/></svg>42 Harbor Lane, Suite B2, Eastmere, MA 02700</span>
  </div>
  <div class="abs contact back-lines">
    <span class="phone"><svg width="8" height="8" viewBox="0 0 8 8"><path d="M1.5 .8l1.4 1.6-.7 1a4 4 0 0 0 2.4 2.4l1-.7 1.6 1.4-.8 1C3.8 7.3.7 4.2.5 1.6z" fill="none" stroke="#fff" stroke-width=".8"/></svg>555-014-2267</span>
    <span><svg width="9" height="7" viewBox="0 0 9 7"><rect x=".5" y=".5" width="8" height="6" fill="none" stroke="#fff" stroke-width=".8"/><path d="M.5.5l4 3.4 4-3.4" fill="none" stroke="#fff" stroke-width=".8"/></svg>info@vornel.example</span>
    <span><svg width="8" height="8" viewBox="0 0 8 8"><circle cx="4" cy="4" r="3.5" fill="none" stroke="#fff" stroke-width=".7"/><ellipse cx="4" cy="4" rx="1.5" ry="3.5" fill="none" stroke="#fff" stroke-width=".7"/><path d="M.5 4h7" stroke="#fff" stroke-width=".7"/></svg>www.vornel.example</span>
  </div>

  <p class="abs route-notice">Our company just insulated a home on your mail route and we'd like to offer you a FREE assessment!</p>

  <div class="abs brand back-brand"><span class="brand-square"></span>Vornel Thermal</div>
  <div class="abs indicia">PRSRT STD<br>ECRWSS<br>U.S. POSTAGE<br>PAID<br>EDDM RETAIL</div>
  <div class="abs route-line">******************************ECRWSS *****</div>
  <div class="abs recipient">Local<br>Postal Customer</div>
</section>

</body>
</html>
```